Chistmas Season Card Design Project

Design a Season's Greetings Card 2021 for a law firm

Target Market(s)

Clients of companies

Industry/Entity Type

Legal

Colors
0054AA
0677BA
7BADD7
CADEEF
E8F1F8
EB3D1F
EC4F4E
F09395
F8D3D4
FCEDEE

```html
<!DOCTYPE html>
<html lang="es">
<head>
<meta charset="utf-8">
<title>Season's Greetings Card 2021</title>
<link rel="stylesheet" href="https://fonts.googleapis.com/css2?family=Allura&family=Montserrat:wght@500;600&display=swap">
<style>
  :root {
    --blue-deep: #0054AA;
    --blue-mid: #0677BA;
    --blue-soft: #7BADD7;
    --blue-pale: #CADEEF;
    --blue-mist: #E8F1F8;
    --paper: #FFFFFF;
    --backdrop: #EEF1F4;
    --panel-shade: #F4F6F8;
  }
  * { box-sizing: border-box; margin: 0; padding: 0; }
  html, body { width: 1200px; height: 840px; overflow: hidden; }
  body {
    background: var(--backdrop);
    font-family: "Montserrat", sans-serif;
    position: relative;
  }
  .card {
    position: absolute;
    left: 200px;
    top: 140px;
    width: 800px;
    height: 560px;
    display: flex;
    box-shadow: 0 6px 24px rgba(0, 40, 80, 0.12);
  }
  .panel {
    position: relative;
    width: 400px;
    height: 560px;
    text-align: center;
  }
  .panel--front {
    background: linear-gradient(180deg, var(--blue-soft) 0%, #6A9FD0 100%);
    color: var(--paper);
  }
  .panel--inside {
    background: linear-gradient(90deg, var(--panel-shade) 0%, var(--paper) 12%, var(--paper) 100%);
    color: var(--blue-mid);
  }
  .greeting-art {
    position: absolute;
    left: 60px;
    top: 60px;
    width: 290px;
    height: 340px;
    background: linear-gradient(180deg, rgba(232, 241, 248, 0.55) 0%, rgba(202, 222, 239, 0.7) 100%);
    display: flex;
    flex-direction: column;
    justify-content: center;
    align-items: center;
  }
  .greeting-art__line {
    font-family: "Allura", cursive;
    color: var(--blue-deep);
    font-size: 52px;
    line-height: 1.15;
  }
  .front-sub {
    position: absolute;
    left: 0;
    right: 0;
    top: 424px;
  }
  .front-sub__and {
    font-size: 9px;
    font-weight: 500;
    display: block;
  }
  .front-sub__wish {
    font-size: 15px;
    font-weight: 500;
    display: block;
    margin-top: 2px;
  }
  .front-rule {
    position: absolute;
    left: 88px;
    top: 470px;
  }
  .firm-name {
    position: absolute;
    left: 0;
    right: 0;
    font-weight: 600;
    text-transform: uppercase;
    letter-spacing: 0.04em;
    line-height: 1.2;
  }
  .panel--front .firm-name {
    top: 490px;
    font-size: 15px;
    color: var(--paper);
  }
  .panel--inside .firm-name {
    top: 418px;
    font-size: 12px;
    color: var(--blue-deep);
  }
  .firm-name__tag { display: block; font-size: 7px; letter-spacing: 0.18em; }
  .inside-greeting {
    position: absolute;
    left: 0;
    right: 0;
    top: 198px;
  }
  .inside-greeting__title {
    font-family: "Allura", cursive;
    font-size: 54px;
    font-weight: 400;
    color: var(--blue-mid);
    line-height: 1.1;
  }
  .inside-greeting__wish {
    font-size: 11px;
    font-weight: 600;
    color: var(--blue-deep);
    margin-top: 8px;
  }
</style>
</head>
<body>
  <main class="card">
    <section class="panel panel--front">
      <div class="greeting-art" role="img" aria-label="Illustration of two stylised blue Christmas trees, stars and a white ribbon banner carrying the Merry Christmas greeting">
        <span class="greeting-art__line">Merry</span>
        <span class="greeting-art__line">Christmas</span>
      </div>
      <p class="front-sub">
        <span class="front-sub__and">and</span>
        <span class="front-sub__wish">Happy New Year!</span>
      </p>
      <svg class="front-rule" width="224" height="10" viewBox="0 0 224 10" aria-hidden="true">
        <line x1="0" y1="5" x2="224" y2="5" stroke="#0054AA" stroke-width="1.5"/>
      </svg>
      <p class="firm-name">Ibarra Montes &amp;<br>Solís Vidal<span class="firm-name__tag">Abogados</span></p>
    </section>
    <section class="panel panel--inside">
      <div class="inside-greeting">
        <h1 class="inside-greeting__title">Feliz navidad</h1>
        <p class="inside-greeting__wish">y próspero año nuevo!</p>
      </div>
      <p class="firm-name">Ibarra Montes &amp;<br>Solís Vidal<span class="firm-name__tag">Abogados</span></p>
    </section>
  </main>
</body>
</html>
```